Plume Chair

A5 Double Sided card for Chair Marketing
This will be our major marketing piece on a stiff piece fo cardboard
Dont feel the need to use all the words below "a picture tells the story" we can trim the words and make sure the message gets out
High end project
Feel free to use the word "plume Chair" innovatively to give it some identity
Want it professional and you can use any of the photos as you see fit
mix up the words etc
• Upholstered in Italian Leather
• High Quality Merino Wool Sheepskins .
• 360 Degree rotation
• Handmade with love and detail
• Cosy
• Calming and unbelievably quiet acoustics
• Unique
This chair is unique and a labor of love and attention to detail, it’s a conversation starter or statement piece. It’s something you just can’t find anywhere.
The acoustics let you escape in any room whether you want to read a book or simply relax
The Drift or Harbor chair
When Ilkka Saranen had the first idea for the Drift Chair
in 1963, fibreglass was a relatively new material as glass reinforced products were not Batch Produced as they are today. The only possibility was to craft the chair with his own hands. It took Ilkka and his brother in law nearly one year until the first prototype was ready.
The prototype was a success, it is still standing in Ilkkas house. By coincidence two young product managers from the company VELMO discovered the Drift Chair when visiting Ilkka in order to look at some pine wood chairs. They immediately realised the potential of this design icon.
In 1966 for the first time the chair was presented at the Northgate Interiors Expo in Cologne. Celebrities bought copies of the original for their homes and it found itself in a variety of Design Museums throughout the world.
The design of the chair was not only striking to look at but it was also comfortable and relaxing to sit in for long periods of time. The chair has been described as ''a room within a room''. It offers shelter, a calming atmosphere and privacy for the seated person.
Our Replica Ilkka Saranen Drift chair is made to exacting standards. The shell is made from solid fiberglass, and is finished in Italian leather. The interior of the ball is padded and covered in lambswool merino sheepskins. The chair is available in different colours.
Feel free to photo shop the chair in front of a lifestyle scene ie an ope fireplace or modern room for a dynamic feel on the front side of the card
Contact details
Tie in the logo loaded as well
We are a small Australian Family creating unique products
RDV
Property of RDV Traders we love to create comfortable and unique things which people talk about and want to adorn their living spaces with.
We hope you love this product as much as we do and have many years enjoyment in it
Please order on our web site www.rdvtraders-example.com.au or email sales@rdvtrd-example.com.au
Lena Whitcombe
Marketing and Sales Manager
0491 237 604
Melbourne, Australia
Niche Market , for private and hotels and high end businesses

```html
<!DOCTYPE html>
<html lang="en">
<head>
<meta charset="utf-8">
<title>Plume Chair – A5 Card</title>
<link rel="stylesheet" href="https://fonts.googleapis.com/css2?family=Cinzel:wght@400;500&family=Source+Sans+3:wght@300;400;600&display=swap">
<style>
  :root{
    --gold:#d4a232;
    --slate:#6b6c70;
    --ink:#3c3c3e;
    --muted:#6f7073;
    --paper:#ffffff;
    --backdrop:#e9e7e4;
  }
  *{box-sizing:border-box;margin:0;padding:0}
  html,body{width:1200px;height:835px;overflow:hidden;background:var(--backdrop)}
  body{position:relative;font-family:"Source Sans 3",Arial,sans-serif;color:var(--ink)}
  .card{position:absolute;top:59px;width:583px;height:826px;background:var(--paper);
        transform:scale(.855);transform-origin:top left;overflow:hidden;
        box-shadow:0 4px 14px rgba(0,0,0,.18)}
  .card--front{left:66px}
  .card--back{left:630px}
  .abs{position:absolute}

  /* brand name set as plain text */
  .brand{font-family:"Source Sans 3",Arial,sans-serif;font-weight:400;font-size:19px;
         letter-spacing:.5px;color:var(--ink);white-space:nowrap}
  .card--back .brand{color:#fff}

  .contact{font-weight:300;font-size:12.5px;line-height:15px;color:var(--muted);text-align:right}
  .title{font-family:"Cinzel",Georgia,serif;font-weight:500;color:#fff;text-align:right;
         font-size:72px;line-height:74px;letter-spacing:1px}

  .photo{position:absolute}
  .photo--room{left:0;top:135px;width:583px;height:306px;
     background:linear-gradient(180deg,#9aa0a4 0%,#c9cdcf 45%,#a9acae 70%,#6d6f72 100%)}
  .photo--studio{left:272px;top:558px;width:311px;height:257px;
     background:linear-gradient(180deg,#f2f2f1 0%,#e6e5e3 55%,#d6cfc4 70%,#c7bfb2 100%)}
  .photo--hero{left:0;top:0;width:583px;height:308px;
     background:linear-gradient(180deg,#8b8d90 0%,#74767a 70%,#9a9a98 82%,#7d7c79 100%)}
  .photo--hearth{left:318px;top:308px;width:265px;height:292px;
     background:linear-gradient(160deg,#6f6c68 0%,#9c9893 45%,#c4c1bc 80%,#b2aea8 100%)}

  .gold-bar{background:var(--gold)}
  .slate-panel{background:var(--slate);color:#fff}

  .features{list-style:none;font-weight:300;font-size:12.5px;line-height:23.6px}
  .features li::before{content:"";display:inline-block;width:4px;height:4px;border-radius:50%;
     background:var(--gold);margin-right:6px;vertical-align:middle}
  .copy{font-weight:300;font-size:12.5px;line-height:15.3px;text-align:justify}
  .copy p+p{margin-top:15px}
  .center{text-align:center}

  .footer{display:flex;justify-content:space-between;align-items:center;
     font-weight:400;font-size:13px;color:var(--gold)}
  .footer span{display:flex;align-items:center;gap:5px}
</style>
</head>
<body>

<!-- FRONT -->
<section class="card card--front">
  <div class="abs brand" style="left:30px;top:92px">RDV UNIQUE PRODUCTS</div>
  <div class="abs contact" style="right:24px;top:36px">
    Lena Whitcombe<br>Marketing and Sales Manager<br>0491 237 604<br>Melbourne, Australia
  </div>
  <div class="abs gold-bar" style="left:272px;top:125px;width:311px;height:10px"></div>

  <div class="photo photo--room" role="img" aria-label="Plume Chair in a minimalist concrete room with large windows onto snowy pines"></div>
  <h1 class="abs title" style="right:30px;top:212px">PLUME<br>CHAIR</h1>

  <ul class="abs features" style="left:22px;top:478px">
    <li>Upholstered in Italian Leather</li>
    <li>High Quality Merino Wool Sheepskins</li>
    <li>360 Degree rotation</li>
    <li>Handmade with love and detail</li>
    <li>Cosy</li>
    <li>Calming and unbelievably quiet acoustics</li>
    <li>Unique</li>
  </ul>
  <div class="abs copy" style="left:20px;top:672px;width:238px">
    <p>Our Replica Ilkka Saranen Drift chair is made to exacting standards. The shell is made from solid fiberglass, and is finished in Italian leather. The interior of the ball is padded and covered in lambswool merino sheepskins.</p>
    <p style="margin-top:9px;text-align:left">The chair is available in different colours.</p>
  </div>

  <div class="abs slate-panel center" style="left:272px;top:441px;width:311px;height:117px;padding-top:32px;font-weight:300;font-size:12.5px;line-height:19.5px">
    The acoustics let you escape in any room<br>whether you want to read a book or simply relax<br>The Drift or Harbor chair
  </div>
  <div class="photo photo--studio" role="img" aria-label="Plume Chair facing forward on a pale timber floor against a white wall"></div>
  <div class="abs gold-bar" style="left:272px;top:815px;width:311px;height:11px"></div>
</section>

<!-- BACK -->
<section class="card card--back">
  <div class="photo photo--hero" role="img" aria-label="Tan leather Plume Chair with sheepskin lining on a pedestal base against a grey wall"></div>
  <div class="abs brand" style="right:20px;top:92px">RDV UNIQUE PRODUCTS</div>
  <h1 class="abs title" style="right:26px;top:124px;font-size:68px;line-height:62px">PLUME<br>CHAIR</h1>

  <div class="abs gold-bar center" style="left:0;top:308px;width:318px;height:95px;padding-top:10px;color:#fff;font-weight:300;font-size:12.5px;line-height:19.5px">
    This chair is unique and a labor of love and<br>attention to detail, it's a conversation starter or<br>statement piece.<br>It's something you just can't find anywhere.
  </div>
  <div class="photo photo--hearth" role="img" aria-label="Plume Chair beside a stacked-stone fireplace with a cushion inside"></div>

  <div class="abs copy" style="left:17px;top:439px;width:275px">
    <p>When Ilkka Saranen had the first idea for the Drift Chair in 1963, fibreglass was a relatively new material as glass reinforced products were not Batch Produced as they are today. The only possibility was to craft the chair with his own hands. It took Ilkka and his brother in law nearly one year until the first prototype was ready.</p>
    <p>In 1966 for the first time the chair was presented at the Northgate Interiors Expo in Cologne. Celebrities bought copies of the original for their homes and it found itself in a variety of Design Museums throughout the world.</p>
    <p>The design of the chair was not only striking to look at but it was also comfortable and relaxing to sit in for long periods of time. The chair has been described as "a room within a room".</p>
    <p>It offers shelter, a calming atmosphere and privacy for the seated person.</p>
  </div>

  <div class="abs slate-panel" style="left:318px;top:603px;width:265px;height:182px;padding:18px 19px 0 10px;text-align:right;font-weight:300;font-size:12.5px;line-height:15px">
    We are a small Australian Family creating<br>unique products
    <p style="color:var(--gold);font-size:11.5px;line-height:16px;margin-top:14px">We hope you love this product as much as we do and have many years enjoyment in it</p>
    <p style="margin-top:8px">Lena Whitcombe<br>Marketing and Sales Manager<br>0491 237 604<br>Melbourne, Australia</p>
  </div>

  <div class="abs footer" style="left:17px;right:14px;top:796px">
    <span><svg width="12" height="12" viewBox="0 0 12 12"><circle cx="6" cy="6" r="5.5" fill="none" stroke="var(--gold)"/><rect x="3" y="4" width="6" height="4" fill="none" stroke="var(--gold)" stroke-width=".9"/><path d="M3 4l3 2.3L9 4" fill="none" stroke="var(--gold)" stroke-width=".9"/></svg>sales@rdvtrd-example.com.au</span>
    <span><svg width="13" height="13" viewBox="0 0 13 13"><circle cx="6.5" cy="6.5" r="6" fill="none" stroke="var(--gold)"/><path d="M4.3 3.5c-.6.6-.3 2.2 1.2 3.7s3.1 1.8 3.7 1.2l.4-.5-1.4-1.1-.7.5c-.6-.2-1.5-1.1-1.7-1.7l.5-.7-1.1-1.4z" fill="var(--gold)"/></svg>0491 237 604</span>
    <span><svg width="12" height="12" viewBox="0 0 12 12"><circle cx="6" cy="6" r="5.5" fill="none" stroke="var(--gold)"/><circle cx="6" cy="6" r="3" fill="none" stroke="var(--gold)" stroke-width=".9"/><path d="M3 6h6M6 3c-1.2 1.6-1.2 4.4 0 6M6 3c1.2 1.6 1.2 4.4 0 6" fill="none" stroke="var(--gold)" stroke-width=".7"/></svg>www.rdvtraders-example.com.au</span>
  </div>
</section>

</body>
</html>
```